Website Graphic Layout

We are looking for someone to provide a crisp clean layout for our new website design.
The site is runs on Drupal & we like the 4 column layout
We think that the current site is a bit cluttered & could be a bit cleaner.

http://www.tovaquen.org/volunteer-abroad

We like the following website as examples as they are quite clean with a large header image & sub areas to add things such as news testimonials etc

http://brastik.com/
http://www.quorvan.com/ie/
http://lantrevoda.org/
http://www.kelvasp.com/

```html
<!DOCTYPE html>
<html lang="en">
<head>
<meta charset="utf-8">
<title>Tovaquen Intercultural Learning</title>
<link rel="stylesheet" href="https://fonts.googleapis.com/css2?family=Arimo:wght@400;700&display=swap">
<style>
  :root {
    --green: #0aa83a;
    --green-dark: #079a33;
    --green-light: #9fe0a8;
    --green-text: #0c9a46;
    --navy: #1d2a7a;
    --magenta: #d0148a;
    --orange: #f7a51b;
    --ink: #111;
    --body: #555;
    --rule: #cfcfcf;
    --footer: #e2e2e2;
    --white: #fff;
  }
  * { margin: 0; padding: 0; box-sizing: border-box; }
  html, body { width: 1200px; height: 1005px; overflow: hidden; background: var(--white); }
  body { position: relative; font-family: "Arimo", Arial, sans-serif; color: var(--ink); }
  .abs { position: absolute; }

  .topbar { left: 0; top: 0; width: 1200px; height: 40px;
    background: linear-gradient(90deg, var(--green-dark) 0%, var(--green) 60%, #6fd07c 100%);
    box-shadow: 0 3px 5px rgba(0,0,0,.25); }
  .social { top: 8px; display: flex; gap: 10px; left: 247px; }
  .social span { width: 24px; height: 24px; border-radius: 50%; background: #dfe8f2; border: 1px solid rgba(255,255,255,.8); }
  .social span:nth-child(2) { background: #3b5a9a; }
  .social span:nth-child(3) { background: #f2f2f2; }
  .social span:nth-child(4) { background: #2c74b3; border-radius: 4px; }
  .mainnav { left: 401px; top: 13px; display: flex; gap: 12px; color: var(--white); font-weight: 700; font-size: 13.5px; letter-spacing: .1px; white-space: nowrap; }
  .search { left: 772px; top: 14px; width: 164px; height: 18px; border-radius: 5px; background: var(--white);
    font-size: 9px; font-weight: 700; padding: 4px 0 0 18px; color: #222; box-shadow: inset 0 1px 2px rgba(0,0,0,.3); }

  .logo { font-weight: 400; color: #14c24a; letter-spacing: -1px; }
  .logo-head { left: 259px; top: 50px; font-size: 45px; }
  .subnav { left: 415px; top: 81px; display: flex; gap: 11px; font-size: 9.5px; font-weight: 700; color: var(--green-text); }
  .subnav .current { color: var(--ink); }
  .subnav .sep { color: #666; font-weight: 400; }

  .rule { height: 1px; background: var(--rule); left: 240px; width: 720px; }

  .hero-band { left: 240px; width: 720px; height: 11px; background: linear-gradient(90deg, var(--green) 50%, var(--green-light)); }
  .hero { left: 240px; top: 142px; width: 720px; height: 264px;
    background: linear-gradient(160deg, #7b5a4a 0%, #a8504a 35%, #3c6d6a 70%, #5a4540 100%); }
  .hero-caption { left: 266px; top: 348px; width: 332px; height: 34px; background: rgba(10,10,10,.88);
    display: flex; justify-content: space-between; align-items: center; padding: 0 14px 0 10px; font-size: 11.5px; font-weight: 700; }
  .hero-caption .tag { color: #ccc; }
  .hero-caption .link { color: var(--orange); }

  .thumb { top: 438px; height: 158px; }
  .thumb-sport { left: 253px; width: 170px; background: linear-gradient(150deg, #2f5a28, #4d7a38 60%, #6f8a4a); }
  .thumb-people { left: 513px; width: 169px; background: linear-gradient(160deg, #b9a98f, #c6b8a0 50%, #545257); }
  .thumb-statue { left: 758px; width: 164px; background: linear-gradient(180deg, #9cbbd8, #b8a79a 55%, #8f7b6c); }
  .view { right: 0; bottom: 0; width: 47px; height: 15px; background: var(--orange); font-size: 8.5px; font-weight: 700;
    color: var(--ink); display: flex; align-items: center; justify-content: center; }

  .col { top: 604px; width: 212px; }
  .col-feature { left: 238px; }
  .col-news { left: 492px; }
  .col-notice { left: 746px; }
  .col .topline { height: 1px; background: var(--rule); }
  .col h2 { font-size: 13.5px; font-weight: 700; margin-top: 3px; padding-left: 22px; position: relative; letter-spacing: .2px; }
  .col h2::before { content: "\2192"; position: absolute; left: 0; top: 0; font-weight: 400; }
  .col-feature h2 { color: var(--green-text); }
  .col-news h2 { color: var(--navy); }
  .col-notice h2 { color: var(--magenta); }
  .col .underline { height: 5px; background: var(--ink); margin-top: 6px; }
  .col p { font-size: 9px; line-height: 15px; color: var(--body); margin-top: 9px; }
  .col-news p { padding-left: 22px; font-size: 8.6px; line-height: 11.4px; margin-top: 8px; letter-spacing: -.1px; }
  .read { left: 242px; top: 770px; font-size: 9px; font-weight: 700; color: var(--orange); }
  .read::before { content: "\2192"; color: var(--ink); margin-right: 8px; font-weight: 400; }

  .promo { top: 800px; width: 323px; height: 122px; border-radius: 4px;
    background: linear-gradient(90deg, var(--green-dark) 0%, var(--green) 45%, #a6e3ac 100%); color: var(--white); font-weight: 700; }
  .promo-contact { left: 260px; }
  .promo-contact .welcome { position: absolute; left: 7px; top: 20px; font-size: 13.5px; white-space: nowrap; }
  .promo-contact .phone { position: absolute; left: 18px; font-size: 17.5px; letter-spacing: .3px; white-space: nowrap; }
  .promo-destinations { left: 622px; padding: 39px 6px 0 43px; font-size: 17px; font-weight: 400; line-height: 15px; letter-spacing: -.1px; }

  .footer { left: 0; top: 929px; width: 1200px; height: 76px; background: var(--footer); }
  .footer-text { left: 256px; top: 940px; font-size: 10px; line-height: 15px; color: #222; white-space: nowrap; }
  .logo-foot { left: 832px; top: 945px; font-size: 41px; font-weight: 700; color: #0bb43b; }
</style>
</head>
<body>
  <header class="abs topbar">
    <div class="abs social" aria-label="Social links"><span></span><span></span><span></span><span></span></div>
    <nav class="abs mainnav"><span>VISIT IRELAND</span><span>|</span><span>ABOUT TOVAQUEN</span><span>|</span><span>COMMUNITY</span></nav>
    <div class="abs search">SEARCH...</div>
  </header>

  <div class="abs logo logo-head">LOGO</div>
  <nav class="abs subnav">
    <span class="current">HOME</span><span class="sep">|</span>
    <span>STUDY ABROAD</span><span class="sep">|</span>
    <span>VOLUNTEER ABROAD</span><span class="sep">|</span>
    <span>DEVELOPMENT EDUCATION</span><span class="sep">|</span>
    <span>TRAVEL AWARDS</span>
  </nav>
  <div class="abs rule" style="top:116px"></div>

  <div class="abs hero-band" style="top:131px"></div>
  <div class="abs hero" role="img" aria-label="Photo of volunteers with local families seated together in a stadium, two holding a hand-made sign"></div>
  <div class="abs hero-band" style="top:406px;height:9px"></div>
  <div class="abs hero-caption"><span class="tag">VOLUNTEER ABROAD</span><span class="link">NEWS AND EVENT &rarr;</span></div>
  <div class="abs rule" style="top:430px"></div>

  <div class="abs thumb thumb-sport" role="img" aria-label="Photo of two students in sports kit on a grass field"><span class="abs view">VIEW &rarr;</span></div>
  <div class="abs thumb thumb-people" role="img" aria-label="Photo of two teachers standing together in a classroom"><span class="abs view">VIEW &rarr;</span></div>
  <div class="abs thumb thumb-statue" role="img" aria-label="Photo of a painted elephant statue against a blue sky"><span class="abs view">VIEW &rarr;</span></div>

  <section class="abs col col-feature">
    <div class="topline"></div>
    <h2>FEATURED PROGRAMME</h2>
    <div class="underline"></div>
    <p>Study Spanish in the tranquil Andalusian town of Nerja. Set on the Mediterranean coast, less than one hour from Malaga Airport and almost equidistant from the famous Andalusian cities of Granada, Seville, Cordoba, Ronda, Nerja is a perfect location for mature students to learn Spanish in small classes while experiencing the life and culture of the Spanish people.</p>
  </section>
  <a class="abs read">READ</a>

  <section class="abs col col-news">
    <div class="topline"></div>
    <h2>NEWS AND EVENTS</h2>
    <div class="underline"></div>
    <p>This week marked six months since I departed from Senya Beraku, Ghana and touched down in Cork on a cold, blustery November morning. What a six months!! Having been struck down with cases of reverse culture shock and many tummy upsets in the Christmas season, I can honestly say that I don't think I felt like the real "Maeve" till at least after the festive season had passed and 2013 had kicked in. This being said life in Ghana and the children of Little Oaks Care were, and still are, constantly on my mind.</p>
  </section>

  <section class="abs col col-notice">
    <div class="topline"></div>
    <h2>ANNOUNCEMENTS</h2>
    <div class="underline"></div>
    <p>New Volunteer Opportunity for Animal Lovers in Jaipur, India!<br><br>This project offers a unique opportunity to gain a basic understanding of the Indian domestic elephant and their relationship with their mahout. You will not only learn how to ride an elephant but also how to care for these intelligent, gentle giants.</p>
  </section>

  <aside class="abs promo promo-contact">
    <span class="welcome">Welcome Guest. Login, Register, Contact us.</span>
    <span class="phone" style="top:62px">LOCALL: 1850 404717</span>
    <span class="phone" style="top:90px">TELEPHONE: 021 4876210</span>
  </aside>
  <aside class="abs promo promo-destinations">Discover our 5 most popular<br>destinations: Vietnam, India,<br>Guatemala, Thailand and Ghana</aside>

  <footer class="abs footer"></footer>
  <div class="abs footer-text">
    Tovaquen Intercultural Learning, 14 Harbour Row, Northfield, Cork, County Cork, Republic of Ireland.<br>
    email: info@tovaquen.org telephone: +353 (0)21 4876210 lowcall: 1850 404717 fax: +353 (0)21 4876244<br>
    cc by-sa 2013 Tovaquen Intercultural Learning
  </div>
  <div class="abs logo logo-foot">LOGO</div>
</body>
</html>
```